Stationery Design Project

KT7 Staffing requires letterhead and business card designs for a company based in London. Just like the name, we're a management resourcing company, providing resources to third party companies. You can see www.kt7staffing-example.com for ideas on existing colour schemes and design concepts that have been implimented and agreed to. Ultimately the design should broadcast professionalism, safety and the concept of growth.

Target Market(s)

Financial institutes; friendly societies (All UK based)

Industry/Entity Type

Safety

Requirements
Must have
• Files produced should be print ready; and the text in them editable (eg address, name etc)

```html
<!DOCTYPE html>
<html lang="en">
<head>
<meta charset="utf-8">
<title>KT7 Staffing — Stationery</title>
<link rel="stylesheet" href="https://fonts.googleapis.com/css2?family=Open+Sans:wght@400;600;700&family=PT+Sans:wght@400&display=swap">
<style>
  :root {
    --teal: #3a8a8c;
    --teal-dark: #378b8d;
    --sky: #81b9c7;
    --card-blue: #3aa3bf;
    --card-glow: #8fd6e6;
    --ink: #3a3a3a;
    --muted: #8a8a8a;
    --name-blue: #5aaec4;
    --paper: #ffffff;
    --stage: #eeeeee;
  }
  * { box-sizing: border-box; margin: 0; padding: 0; }
  html, body { width: 1200px; height: 900px; overflow: hidden; }
  body {
    position: relative;
    background: radial-gradient(circle at 75% 40%, #ffffff 0%, #f4f4f4 45%, var(--stage) 100%);
    font-family: "Open Sans", Arial, sans-serif;
  }

  /* Letterhead */
  .letterhead {
    position: absolute; left: 73px; top: 55px; width: 611px; height: 792px;
    background: var(--paper);
    box-shadow: 0 0 6px rgba(0,0,0,.05);
  }
  .brand {
    position: absolute; display: flex; align-items: center; gap: 10px;
    font-family: "Open Sans", Arial, sans-serif; font-weight: 700; color: var(--teal);
    white-space: nowrap;
  }
  .brand-dot { border-radius: 50%; background: currentColor; flex: none; }
  .letterhead .brand { left: 25px; top: 48px; font-size: 30px; }
  .letterhead .brand-dot { width: 30px; height: 30px; }

  .letter-body {
    position: absolute; left: 78px; top: 200px; width: 448px;
    font-family: "PT Sans", Verdana, sans-serif; font-size: 10px; line-height: 12px;
    color: var(--ink); text-align: justify;
  }
  .letter-body p + p { margin-top: 12px; }

  .signature {
    position: absolute; left: 81px; top: 605px; width: 101px; height: 70px;
    background: #f2f2f2; border-radius: 4px;
  }

  .letter-address {
    position: absolute; left: 25px; top: 711px;
    font-size: 10px; line-height: 13.5px; color: var(--ink);
  }
  .letter-address .label { color: var(--sky); }

  .band { position: absolute; left: 0; right: 0; bottom: 0; background: var(--sky); display: flex; justify-content: flex-end; }
  .band-accent { background: var(--teal-dark); color: #fff; display: flex; align-items: center; justify-content: center; }
  .letterhead .band { height: 21px; }
  .letterhead .band-accent { width: 187px; font-size: 10px; }

  /* Business cards */
  .card {
    position: absolute; left: 758px; width: 252px; height: 144px;
    border-radius: 10px; overflow: hidden;
  }
  .card-front {
    top: 129px;
    background: radial-gradient(ellipse at 50% 45%, var(--card-glow) 0%, var(--card-blue) 60%, #3299b6 100%);
  }
  .card-front .brand { left: 50%; top: 50%; transform: translate(-50%, -50%); color: #fff; font-size: 20px; gap: 7px; }
  .card-front .brand-dot { width: 18px; height: 18px; }

  .card-back { top: 300px; background: var(--paper); }
  .card-back .brand { left: 9px; top: 14px; font-size: 19px; gap: 6px; }
  .card-back .brand-dot { width: 17px; height: 17px; }

  .card-address {
    position: absolute; left: 17px; top: 63px;
    font-size: 5.5px; line-height: 8px; color: var(--muted);
  }
  .card-contacts {
    position: absolute; left: 17px; top: 87px; list-style: none;
    font-size: 5.5px; line-height: 8.4px; color: var(--muted);
  }
  .card-contacts li { display: flex; align-items: center; gap: 5px; }
  .card-contacts svg { width: 6px; height: 6px; fill: var(--sky); flex: none; }

  .card-person { position: absolute; right: 21px; top: 89px; text-align: right; }
  .person-name { font-size: 9.5px; font-weight: 600; color: var(--name-blue); line-height: 12px; }
  .person-role { font-size: 5.5px; color: var(--muted); }

  .card-back .band { height: 12px; }
  .card-back .band-accent { width: 94px; }
</style>
</head>
<body>

<section class="letterhead" aria-label="Letterhead">
  <div class="brand"><span class="brand-dot"></span>KT7 Staffing</div>

  <div class="letter-body">
    <p>Lorem ipsum dolor sit amet, consectetuer adipiscing elit. Pellentesque tristique elementum sem. Quisque eget erat ac lectus sodales faucibus. Nam commodo est. Cras consequat faucibus velit. Nam ac magna. Sed et ligula. Nam volutpat, elit ac facilisis tempor, neque augue euismod leo, sit amet molestie sem est eu libero. Nulla facilisi. Pellentesque sit amet odio. Curabitur a leo consectetuer leo blandit porttitor. Pellentesque velit quam, gravida at, pharetra eu, convallis non, sem. Aenean tempor nibh at purus. Pellentesque porta. Suspendisse congue, lacus sit amet imperdiet imperdiet, urna massa rutrum urna, id elementum tellus diam quis risus.</p>
    <p>In dui turpis, varius vitae, tincidunt id, consequat ut, leo. Donec tincidunt tristique odio. Nulla erat felis, euismod nec, fringilla non, aliquet et, magna. Nulla at magna quis nisi pretium vehicula. Pellentesque habitant morbi tristique senectus et netus et malesuada fames ac turpis egestas. Class aptent taciti sociosqu ad litora torquent per conubia nostra, per inceptos himenaeos. In vel quam. Phasellus varius convallis purus. In non turpis. Nam sed risus. Etiam non neque at nisl gravida porttitor. Donec leo dolor, feugiat ut, pharetra et, porttitor a, metus. Suspendisse laoreet magna vel elit. Ut est augue, fermentum ac, molestie at, vestibulum et, urna.</p>
    <p>Nunc purus. Cras auctor. In ornare neque id ipsum. Nulla tincidunt, diam sit amet viverra euismod, sapien augue fringilla neque, at pellentesque felis tortor vel enim. Etiam dignissim. Sed a tortor vel nisl euismod ultricies. Donec molestie congue lectus. Integer sed turpis a tortor imperdiet consequat. Maecenas molestie placerat urna. Sed pede enim, sollicitudin nec, pretium nec, sollicitudin a, felis. In hac habitasse platea dictumst. Nam facilisis, tellus non scelerisque placerat, turpis turpis semper ante, euismod imperdiet augue nisi et neque. Vivamus tincidunt.</p>
    <p>Nulla lobortis ultricies nulla. Pellentesque purus mi, consequat quis, hendrerit sed, imperdiet non, eros. Nullam urna est, vehicula nec, cursus nec, dignissim sit amet, risus. Duis molestie, tellus sit amet laoreet ullamcorper, urna nisi fringilla ante, at rhoncus justo dolor vel dui. Nam hendrerit luctus lorem. Aenean tempor, metus vel posuere gravida, arcu nunc imperdiet tellus, ut blandit sem magna a turpis. Vivamus in neque. Lorem ipsum dolor sit amet, consectetuer adipiscing elit. Duis tristique tortor id nisl feugiat posuere. Maecenas posuere nisi ac risus. Nunc hendrerit. Praesent porta tempus ligula. Morbi in leo. Curabitur sapien nulla, cursus eget, faucibus in, porttitor et, odio. Praesent sed justo sed arcu commodo feugiat. Duis facilisis nulla ut eros. Cras libero. Donec mollis consectetuer metus. Praesent odio.</p>
  </div>

  <div class="signature" role="img" aria-label="Handwritten signature"></div>

  <address class="letter-address" style="font-style:normal">
    48 Harrow Lane, Suite<br>
    Millbrook, TN&nbsp; 30010<br>
    <span class="label">Phone.</span> 555-010-4477<br>
    <span class="label">Fax.</span> 555-010-4477
  </address>

  <div class="band"><div class="band-accent">www.kt7staffing-example.com</div></div>
</section>

<section class="card card-front" aria-label="Business card, front">
  <div class="brand"><span class="brand-dot"></span>KT7 Staffing</div>
</section>

<section class="card card-back" aria-label="Business card, back">
  <div class="brand"><span class="brand-dot"></span>KT7 Staffing</div>

  <address class="card-address" style="font-style:normal">
    48 Harrow Lane, Suite 7<br>
    Millbrook, TN&nbsp; 30010
  </address>

  <ul class="card-contacts">
    <li><svg viewBox="0 0 10 10"><path d="M1 3 Q5 0 9 3 L8 5 L6 4 L4 4 L2 5 Z M2 6 H8 V9 H2 Z"/></svg>0044 (0)300 000 0101</li>
    <li><svg viewBox="0 0 10 10"><rect x="3" y="0" width="4" height="10" rx="1"/></svg>0044 (0)7700 900 123</li>
    <li><svg viewBox="0 0 10 10"><rect x="2" y="0" width="6" height="3"/><rect x="0" y="4" width="10" height="6" rx="1"/></svg>0044 (0)300 000 0102</li>
    <li><svg viewBox="0 0 10 10"><path d="M0 2 H10 V9 H0 Z M0 2 L5 6 L10 2" /></svg>info@kt7staffing-example.com</li>
    <li><svg viewBox="0 0 10 10"><path d="M5 0 L10 5 H8.5 V10 H1.5 V5 H0 Z"/></svg>www.kt7staffing-example.com</li>
  </ul>

  <div class="card-person">
    <div class="person-name">Daniel Marsh</div>
    <div class="person-role">Marketing Manager</div>
  </div>

  <div class="band"><div class="band-accent"></div></div>
</section>

</body>
</html>
```